Unique Beautiful Realtor business card

I need a unique business card that includes my logo, my firms logo, my picture and phone number. The colors should compliment my logo.

Target Market(s)

People who want to buy or sell a home in South Florida

Contact Information for Business Card

Use two sides and work with the DRM Coastal Homes logo as a theme.
The Harlow Benton should be small and discreet, it is a requirement to be there but should be small. My photo should be integrated artistically.

Font styles to use
Serif
Sans Serif

Colors

Designer to choose colors to be used in the design.

Requirements
Must have
• My logo, Harlow Benton logo, my photo, my phone number, (954-283-6091) and my website address. (www.drmcoastalhomes.example)
• Also my name, Dana R. Moreland, PA, Realtor
• Also “The Pet Friendly Realtor”

```html
<!DOCTYPE html>
<html lang="en">
<head>
<meta charset="utf-8">
<title>DRM Coastal Homes – Business Card</title>
<link href="https://fonts.googleapis.com/css2?family=Roboto:ital,wght@0,400;0,500;0,700;1,500&display=swap" rel="stylesheet">
<style>
  :root {
    --stage: #e9eaec;
    --card: #ffffff;
    --navy: #08457c;
    --sky: #1a8fd0;
    --olive: #a8a81c;
    --text: #4a4a4a;
    --rule: #8a8a8a;
    --photo-top: #c9b79a;
    --photo-bottom: #3a3a40;
  }
  * { box-sizing: border-box; margin: 0; padding: 0; }
  html, body { width: 1125px; height: 1200px; overflow: hidden; }
  body {
    background: var(--stage);
    font-family: "Roboto", Arial, sans-serif;
    position: relative;
  }
  .card {
    position: absolute;
    left: 171px;
    width: 826px;
    height: 470px;
    overflow: hidden;
  }
  .card--front { top: 106px; background: var(--card); }
  .card--back { top: 640px; background: var(--navy); }

  .brand {
    position: absolute;
    left: 466px; top: 38px;
    width: 307px; height: 167px;
    display: flex; align-items: center; justify-content: center; gap: 12px;
  }
  .brand__dot {
    width: 22px; height: 22px; border-radius: 50%;
    background: var(--olive); flex: none;
  }
  .brand__name {
    font-size: 30px; font-weight: 700; color: var(--navy);
    line-height: 1.1;
  }

  .portrait {
    position: absolute;
    left: 47px; top: 135px;
    width: 115px; height: 132px;
    border: 1px solid #9a9a9a;
    border-radius: 5px;
    background: linear-gradient(180deg, var(--photo-top), var(--photo-bottom));
  }

  .agent { position: absolute; left: 45px; top: 276px; }
  .agent__name { font-size: 31px; font-weight: 700; color: var(--navy); line-height: 1.1; }
  .agent__role { font-size: 21px; font-weight: 500; color: var(--sky); line-height: 1.2; }

  .rule {
    position: absolute; left: 47px; top: 348px;
    width: 732px; height: 1px; background: var(--rule);
  }

  .contacts {
    position: absolute; left: 47px; top: 362px;
    list-style: none;
  }
  .contacts li {
    display: flex; align-items: center; gap: 11px;
    font-size: 19.5px; color: var(--text); height: 26.5px;
  }
  .contacts svg { width: 18px; height: 18px; fill: var(--navy); flex: none; }

  .tagline {
    position: absolute; right: 47px; top: 411px;
    font-size: 19.5px; font-style: italic; font-weight: 500; color: var(--navy);
  }

  .stripe { position: absolute; left: 0; bottom: 0; width: 826px; height: 12px; }

  .back-brand {
    position: absolute; left: 0; right: 0; top: 160px;
    display: flex; align-items: center; justify-content: center; gap: 16px;
  }
  .back-brand__dot { width: 34px; height: 34px; border-radius: 50%; background: #ffffff; }
  .back-brand__name { font-size: 50px; font-weight: 700; color: #ffffff; }

  .back-web {
    position: absolute; left: 0; right: 0; top: 406px;
    text-align: center; font-size: 19.5px; letter-spacing: 6px; color: #ffffff;
  }
</style>
</head>
<body>

<section class="card card--front">
  <div class="brand">
    <span class="brand__dot"></span>
    <span class="brand__name">DRM Coastal Homes</span>
  </div>

  <div class="portrait" role="img" aria-label="Portrait photo of Dana R. Moreland"></div>

  <div class="agent">
    <p class="agent__name">Dana R. Moreland, PA</p>
    <p class="agent__role">Realtor</p>
  </div>

  <div class="rule"></div>

  <ul class="contacts">
    <li>
      <svg viewBox="0 0 24 24" aria-hidden="true"><path d="M6.6 10.8a15.1 15.1 0 0 0 6.6 6.6l2.2-2.2c.3-.3.7-.4 1-.2 1.1.4 2.3.6 3.6.6.6 0 1 .4 1 1V20c0 .6-.4 1-1 1A17 17 0 0 1 3 4c0-.6.4-1 1-1h3.5c.6 0 1 .4 1 1 0 1.3.2 2.5.6 3.6.1.3 0 .7-.2 1z"/></svg>
      (954-283-6091)
    </li>
    <li>
      <svg viewBox="0 0 24 24" aria-hidden="true"><path d="M2 5h20v14H2zm2 2v.3l8 5.2 8-5.2V7zm0 2.7V17h16V9.7l-8 5.2z"/></svg>
      info@drmcoastalhomes.example
    </li>
    <li>
      <svg viewBox="0 0 24 24" aria-hidden="true"><circle cx="12" cy="12" r="10"/><path d="M7 8c2 0 3 1 3 3s-2 2-2 4l-2 1c-1-2-1-6 1-8zm8-3c1 1 0 3 2 3l2 2c0 3-2 3-3 5l-1-3-2-1 1-3z" fill="#fff"/></svg>
      www.drmcoastalhomes.example
    </li>
  </ul>

  <p class="tagline">The Pet Friendly Realtor</p>

  <svg class="stripe" viewBox="0 0 826 12" preserveAspectRatio="none" aria-hidden="true">
    <polygon points="0,0 471,0 467,12 0,12" fill="var(--navy)"/>
    <polygon points="475,0 826,0 826,12 471,12" fill="var(--olive)"/>
  </svg>
</section>

<section class="card card--back">
  <div class="back-brand">
    <span class="back-brand__dot"></span>
    <span class="back-brand__name">DRM Coastal Homes</span>
  </div>
  <p class="back-web">www.drmcoastalhomes.example</p>
</section>

</body>
</html>
```